Redesign of ormavue.com website (3 page types)

We need a fresh rebrush of www.ormavue.com, a portal for french regions, departements and cities. It shall look modern as the current design is over 10 years old.

We like the blueish colors and the french touch (blue, white, red).

There are 3 page types that we currently need:
- Homepage (http://www.ormavue.com/)
- Region overview (e.g. http://www.ormavue.com/provence-alpes-cote-d-azur)
- City overview (e.g. http://www.ormavue.com/provence-alpes-cote-d-azur/bouches-du-rhone/marseille)

See "Must have" for a more detailed briefing. All required elements exist and need a rebrush/redesign

Requirements
Must have
• General:

- 3 column layout
+ Header
+ Left sidebar
+ Content area
+ Right sidebar (250px inner width for ads)
+ Footer
- 3 classes of headlines
- Simple sidebar widgets (headline & content / without headline)

Header:
- Logo
- 2 or 3 links
- Search box
- Breadcrumb navigation

Footer:
- Nothing special, really

Homepage:
- Nice looking map with visible region borders to create a mouseover effect (as seen on current version). Meaning we need the plain map and a version with each region highlighted
- Text areas
- Content boxes (like the current gray ones)

Region overview
- Headline
- Info box (Informations)
- Mini map
- Crest / emblem
- Text area with headline for a long descriptive text with a "read more" / "show less" button/link to pop out the whole text via javascript
- List of the 24 biggest cities in the region

City overview
- Headline
- Info box (Informations, same look as for regions)
- Mini map
- List of the 24 cities nearby
- List of available photos
- Example sidebar widgets (right sidebar):
+ Upload a photo of this city
+ Weather conditions
+ Link list
Nice to have
• - A new favicon
- Pindora og:image
Should not have
• - Flash
- Animations

```html
<!DOCTYPE html>
<html lang="fr">
<head>
<meta charset="utf-8">
<title>ormavue.com – Les villes de France</title>
<link rel="stylesheet" href="https://fonts.googleapis.com/css2?family=Arimo:wght@400;700&display=swap">
<style>
:root{
  --blue:#1f4d9f;
  --blue-dark:#163c82;
  --link:#2b51a8;
  --red:#cc1f1f;
  --text:#555;
  --text-dark:#222;
  --line:#dcdcdc;
  --page:#e7e7e7;
  --side:#f6f6f6;
  --white:#fff;
  --footer:#333;
}
*{box-sizing:border-box;margin:0;padding:0}
html,body{width:713px;height:1200px;overflow:hidden}
body{position:relative;background:var(--page);font-family:"Arimo",Arial,sans-serif;color:var(--text);font-size:7.4px;line-height:1.32}
a{color:inherit;text-decoration:none}
.abs{position:absolute}

/* header */
.site-header{position:absolute;left:0;top:0;width:713px;height:39px;background:linear-gradient(#2458ae,var(--blue-dark))}
.brand{position:absolute;left:22px;top:9px;color:var(--white);font-size:18px;font-weight:700;letter-spacing:.2px}
.main-nav{position:absolute;left:360px;top:17px;color:var(--white);font-size:8px;display:flex;gap:6px}
.main-nav .sep{opacity:.8}
.search{position:absolute;left:585px;top:13px;width:106px;height:15px;background:var(--white);border:1px solid #9fb2d6}
.search svg{position:absolute;right:3px;top:2px}
.hero{position:absolute;left:0;top:39px;width:713px;height:145px;background:linear-gradient(180deg,#8fb8d8 0%,#6f9a55 45%,#c9a77a 62%,#3f6b3c 100%)}

/* columns */
.frame{position:absolute;left:22px;top:184px;width:670px;height:990px;background:var(--white)}
.sidebar{position:absolute;top:184px;height:990px;background:var(--side)}
.sidebar.left{left:22px;width:118px;border-right:1px solid var(--line)}
.sidebar.right{left:534px;width:158px;border-left:1px solid var(--line)}
.widget-title{font-size:12px;color:var(--text-dark);padding-bottom:3px;border-bottom:2px solid var(--red);width:100%}
.link-list{list-style:none}
.link-list li{height:16.7px;line-height:16.5px;border-bottom:1px solid #e2e2e2;padding-left:7px;font-size:7.6px;color:#444}
.link-list li.active{background:#ececec}

/* left column */
.left-block{position:absolute;left:29px;width:101px}
.social-box{position:absolute;left:29px;top:656px;width:101px;height:152px;background:var(--white);border:1px solid #c9c9c9;padding:4px}
.social-head{display:flex;gap:4px}
.avatar{background:#d7dce6;border:1px solid #bbb}
.social-name{color:var(--link);font-weight:700;font-size:7px}
.social-sub{color:var(--link);font-size:6px}
.like-btn{display:inline-block;margin-top:2px;width:20px;height:7px;background:#e8ebf2;border:1px solid #b9c2d6}
.social-count{margin-top:6px;padding-top:4px;border-top:1px solid #ddd;font-size:5.8px;color:#333}
.social-count b{color:var(--link)}
.fans{display:grid;grid-template-columns:repeat(3,26px);gap:4px 4px;margin-top:6px;padding-left:2px}
.fan{font-size:5px;text-align:center;color:#444}
.fan .avatar{width:26px;height:28px;margin-bottom:2px;background:#e3e8f1}
.social-foot{position:absolute;left:4px;bottom:3px;font-size:5.5px;color:#333;display:flex;align-items:center;gap:3px}
.social-foot i{display:block;width:7px;height:7px;background:var(--blue)}

/* content */
.content{position:absolute;left:161px;width:352px}
.section-title{font-size:12px;color:var(--text-dark)}
.lead{font-size:8px;color:#333;margin-top:2px}
.prose p{text-align:justify;margin-bottom:8px}
.divider{position:absolute;left:161px;width:352px;border-top:1px dotted #b7b7b7}
.city-link{color:var(--link)}
.photo{border:1px solid #ccc;padding:2px;background:var(--white)}
.photo .fill{width:100%;height:100%}
.news-title{position:absolute;left:161px;font-size:8.4px;color:var(--red)}
.news-photo{position:absolute;left:163px;width:94px;height:63px}
.news-text{position:absolute;left:267px;width:246px;text-align:justify}
.more{position:absolute;right:200px;font-size:7.6px;color:var(--link)}

/* right column */
.ad{position:absolute;left:543px;width:139px;height:139px;background:#e2e2e2;display:flex;align-items:center;justify-content:center;font-size:15px;color:#111}

/* footer */
.site-footer{position:absolute;left:0;top:1174px;width:713px;height:26px;background:var(--footer);border-top:2px solid var(--red);color:#eee;font-size:7.2px;text-align:center;line-height:23px}
</style>
</head>
<body>

<header class="site-header">
  <a class="brand" href="#">ormavue.com</a>
  <nav class="main-nav">
    <a href="#">Maison</a><span class="sep">|</span>
    <a href="#">Les régions</a><span class="sep">|</span>
    <a href="#">Grandes villes</a><span class="sep">|</span>
    <a href="#">Contactez</a>
  </nav>
  <div class="search">
    <svg width="10" height="10" viewBox="0 0 10 10"><circle cx="4" cy="4" r="3" fill="none" stroke="#888" stroke-width="1.2"/><line x1="6.2" y1="6.2" x2="9" y2="9" stroke="#888" stroke-width="1.4"/></svg>
  </div>
</header>
<div class="hero" role="img" aria-label="Photo panoramique d'un village français au bord d'une rivière sous des falaises boisées"></div>

<div class="frame"></div>
<aside class="sidebar left"></aside>
<aside class="sidebar right"></aside>

<!-- left sidebar -->
<section class="left-block" style="top:196px">
  <h3 class="widget-title">Les régions</h3>
  <ul class="link-list" style="margin-top:3px">
    <li>Alsace</li><li>Aquitaine</li><li>Auvergne</li><li>Basse-Normandie</li><li>Bourgogne</li><li>Bretagne</li><li class="active">Centre</li><li>Champagne-Ardenne</li><li>Corse</li><li>Franche-Comté</li><li>Haute-Normandie</li><li>Île-de-France</li><li>Languedoc-Roussillon</li><li>Limousin</li><li>Lorraine</li><li>Midi-Pyrénées</li><li>Nord-Pas-de-Calais</li><li>Pays de la Loire</li><li>Picardie</li><li>Poitou-Charentes</li><li>Provence-Alpes-Côte</li><li>Rhône-Alpes</li>
  </ul>
</section>
<section class="left-block" style="top:598px">
  <h3 class="widget-title">La France</h3>
  <p style="margin-top:9px;font-size:7.6px;color:#444;padding-left:0">Statistique</p>
</section>
<section class="social-box">
  <div class="social-head">
    <div class="avatar" style="width:20px;height:20px"></div>
    <div>
      <div class="social-name">ormavue.com</div>
      <div class="social-sub">on Pindora</div>
      <span class="like-btn"></span>
    </div>
  </div>
  <div class="social-count">5,000 people like <b>ormavue.com</b></div>
  <div class="fans">
    <div class="fan"><div class="avatar"></div>Thing 1</div>
    <div class="fan"><div class="avatar"></div>Thing 2</div>
    <div class="fan"><div class="avatar"></div>Apples</div>
    <div class="fan"><div class="avatar"></div>Wayne</div>
    <div class="fan"><div class="avatar"></div>Carth</div>
    <div class="fan"><div class="avatar"></div>Bill</div>
  </div>
  <div class="social-foot"><i></i>Pindora social plugin</div>
</section>

<!-- content -->
<section class="content" style="top:196px">
  <h1 class="section-title">Les villes de France</h1>
  <p class="lead">Trouvez ici les régions, départements et villes français.</p>
</section>
<div class="abs" role="img" aria-label="Carte des régions de France en bleu, la région Rhône-Alpes surlignée en rouge" style="left:232px;top:234px;width:218px;height:250px;background:linear-gradient(135deg,#1c3d93,#14338a 70%,#b81515 100%);border-radius:30px 40px 20px 50px"></div>
<section class="content prose" style="top:493px">
  <p>Vous vous trouvez sur un site web dédié à vous donner toutes les informations dont vous avez besoin: Nous vous mettons à disposition une liste complète indiquant toutes les villes et tous les villages de France avec leurs codes postaux et des informations touristiques. Vous pouvez aussi télécharger les plus jolies photos de votre ville.</p>
  <p>En plus, vous trouvez ici des annonces immobilières qui vous aident à trouver la maison de vos rêves, des locaux appropriés pour votre nouveau bureau ou un petit appartement au centre-ville.</p>
  <p>Plusieurs informations supplémentaires, comme le service de météo, la possibilité d'inscrire votre propre siteweb lié à votre ville et les actualités locaux, rendent complèt le total de notre offerte gratuite.</p>
</section>
<div class="divider" style="top:617px"></div>

<section class="content prose" style="top:630px">
  <h2 class="section-title">Les plus belles villes du mois</h2>
  <p style="margin-top:9px">La « capitale européenne » <span class="city-link">Strasbourg</span> est aussi la capitale historique de l'Alsace à l'est de la France. Strasbourg compte 272 500 habitants et est aussi le chef-lieu du département Bas-Rhin. Au fil du développement de l'union européenne, Strasbourg, aussi à cause de sa situation géographique à la frontière franco-allemande, est devenue siège d'un grand nombre d'institutions européennes, entre autres : Le Conseil de l'Europe, le Parlement européen et la Cour Européenne des droits de l'homme.</p>
</section>
<div class="photo abs" style="left:163px;top:724px;width:95px;height:64px"><div class="fill" role="img" aria-label="Vue de Marseille et de la mer" style="background:linear-gradient(#a9c4dc,#7f9fb9 55%,#8a7d63)"></div></div>
<section class="content prose" style="top:724px">
  <p style="margin-left:105px">Marseille n'est pas seulement la ville la plus âgée de la France - à cause de son important port commercial, elle est aussi appelée « la porte au monde ». Fondée en 600 avant J.-C. par des marins Grecs de Phocée, Marseille est le premier port de la France. Marseille est le siège d'un archevêque, ville d'université et capitale de départements Bouches-du-Rhône. La ville doit son expansion et prospérité à son port, qui est un lieu de transbordement important pour des marchandises destinées pour l'Afrique du Nord et l'Asie. Spécialement le pétrole occupe une position éminente...</p>
</section>
<div class="divider" style="top:826px"></div>

<section class="content" style="top:838px"><h2 class="section-title">Actualités locales</h2></section>

<h3 class="news-title" style="top:863px">Russie: une Nova Riot en grève de la faim pour protester contre le tribunal</h3>
<div class="photo news-photo" style="top:882px"><div class="fill" role="img" aria-label="Photo d'actualité" style="background:linear-gradient(135deg,#4a3a2c,#8a6a4c)"></div></div>
<p class="news-text" style="top:881px">Une jeune femme du groupe contestataire russe Nova Riot emprisonnée a entamé mercredi une grève de la faim après avoir été empêchée par la justice d'assister à l'audience sur sa demande de libération anticipée.</p>
<a class="more" href="#" style="top:937px">Savoir plus...</a>
<div class="divider" style="top:959px"></div>

<h3 class="news-title" style="top:970px">Russie: une Nova Riot en grève de la faim pour protester contre le tribunal</h3>
<div class="photo news-photo" style="top:987px"><div class="fill" role="img" aria-label="Photo d'actualité" style="background:linear-gradient(135deg,#4a3a2c,#8a6a4c)"></div></div>
<p class="news-text" style="top:986px">Une jeune femme du groupe contestataire russe Nova Riot emprisonnée a entamé mercredi une grève de la faim après avoir été empêchée par la justice d'assister à l'audience sur sa demande de libération anticipée.</p>
<a class="more" href="#" style="top:1043px">Savoir plus...</a>
<div class="divider" style="top:1064px"></div>

<h3 class="news-title" style="top:1075px">Russie: une Nova Riot en grève de la faim pour protester contre le tribunal</h3>
<div class="photo news-photo" style="top:1091px"><div class="fill" role="img" aria-label="Photo d'actualité" style="background:linear-gradient(135deg,#4a3a2c,#8a6a4c)"></div></div>
<p class="news-text" style="top:1091px">Une jeune femme du groupe contestataire russe Nova Riot emprisonnée a entamé mercredi une grève de la faim après avoir été empêchée par la justice d'assister à l'audience sur sa demande de libération anticipée.</p>
<a class="more" href="#" style="top:1147px">Savoir plus...</a>

<!-- right sidebar -->
<section class="abs" style="left:543px;top:196px;width:139px">
  <h3 class="widget-title">Les plus grandes villes</h3>
  <ul class="link-list" style="margin-top:3px">
    <li>Paris</li><li>Marseille</li><li>Lyon</li><li>Toulouse</li><li>Nice</li><li>Nantes</li><li>Strasbourg</li><li>Montpellier</li><li>Bordeaux</li><li>Lille</li><li>Rennes</li><li>Le Havre</li><li>Reims</li><li>Saint-Étienne</li><li>Toulon</li><li>Grenoble</li><li>Angers</li><li>Dijon</li><li>Brest</li><li>Le Mans</li><li>Clermont-Ferrand</li><li>Amiens</li><li>Aix-en-Provence</li><li>Limoges</li><li>Nîmes</li>
  </ul>
</section>
<div class="ad" style="top:651px">250 x 250</div>
<div class="ad" role="img" aria-label="Bannière publicitaire pour un emploi à domicile" style="top:807px;background:linear-gradient(160deg,#f07a10,#f4a21a 45%,#1e5bb5)"></div>
<div class="ad" style="top:962px">250 x 250</div>

<footer class="site-footer">Copyright © 2013 ormavue.com. All Rights Reserved.</footer>

</body>
</html>
```